SUMMIT GATHERING 2021. August 20th -22nd.

The Hosts of the conference: Grace Tabernacle-Pastors Ron n Della ( Picture with two persons)

Guest Minister: Bishop Lucinda Okotieno. (Cedar Ridge Awakening)

Venue:
Sealand Gateway Lodgeview. 4817 North 239th Avenue Seattle, WA 98174.

Conference times.
Friday August 20th 6pm-8:30pm
Saturday August 21st. 6pm-8:30pm

Sunday August 22nd 10am-1pm
“ CHURCH RENEWAL GATHERING”

5pm-7:30pm
TWOFOLD SURGE GATHERING.

Target Market(s)

18-55

Industry/Entity Type

Religious/ Entertainment.

Requirements
Must have
• A highlight of the Relaunch service on Sunday August 22nd 5pm-7:30pm.
Nice to have
• Excellent ideas….

```html
<!DOCTYPE html>
<html lang="en">
<head>
<meta charset="utf-8">
<title>Grace Tabernacle – Summit Gathering 2021</title>
<link href="https://fonts.googleapis.com/css2?family=Barlow:wght@300;400;500;600;700&family=Barlow+Semi+Condensed:wght@500;600&display=swap" rel="stylesheet">
<style>
  :root{
    --red-deep:#7d0709;
    --red:#a31014;
    --red-bright:#bf1a1f;
    --cream:#e7d7a6;
    --ink:#222222;
    --gold:#c9a86a;
  }
  *{margin:0;padding:0;box-sizing:border-box}
  html,body{width:1200px;height:944px;overflow:hidden;background:var(--red-deep)}
  .flyer{
    position:relative;width:1200px;height:944px;overflow:hidden;
    font-family:"Barlow",sans-serif;color:var(--cream);
  }
  .flyer__backdrop{
    position:absolute;inset:0;
    background:
      radial-gradient(ellipse at 45% 30%, rgba(230,40,45,.45), transparent 60%),
      radial-gradient(ellipse at 80% 80%, rgba(120,5,8,.6), transparent 60%),
      linear-gradient(160deg,var(--red-bright),var(--red) 45%,var(--red-deep));
  }
  .flyer__frame{
    position:absolute;left:31px;top:24px;width:1139px;height:896px;
    border:1.5px solid var(--cream);opacity:.85;
  }
  .event{
    position:absolute;left:88px;top:46px;font-size:20px;font-weight:600;
    letter-spacing:2px;white-space:nowrap;
  }
  .event__dates{font-weight:400;letter-spacing:1px}
  .title{
    position:absolute;left:87px;top:88px;display:flex;align-items:center;gap:14px;
    line-height:1;
  }
  .title__bold{font-weight:700;font-size:80px;letter-spacing:1px;color:var(--cream)}
  .title__boxed{
    font-weight:400;font-size:72px;color:var(--ink);background:var(--cream);
    padding:8px 8px 6px;
  }
  .venue__label{position:absolute;left:81px;top:216px;font-size:24px;font-weight:500}
  .venue__address{
    position:absolute;left:80px;top:254px;width:714px;height:29px;border-radius:8px;
    background:var(--cream);color:var(--ink);font-size:20px;font-weight:500;
    display:flex;align-items:center;padding-left:12px;letter-spacing:.3px;
  }
  .guest__tag{
    position:absolute;left:80px;top:315px;width:312px;height:46px;
    border:1.5px solid var(--cream);border-radius:12px;
    font-size:35px;font-weight:500;display:flex;align-items:center;justify-content:center;
  }
  .guest__name{
    position:absolute;left:80px;top:366px;white-space:nowrap;
    font-family:"Barlow Semi Condensed",sans-serif;font-weight:600;font-size:44px;
  }
  .guest__church{font-family:"Barlow",sans-serif;font-weight:400;font-size:17px}
  .portrait{
    position:absolute;border-radius:50%;border:4px solid var(--cream);
  }
  .portrait--hosts{
    left:829px;top:71px;width:290px;height:290px;
    background:radial-gradient(circle at 40% 45%,#8a5a3e,#3b2440 55%,#5b2a8a);
  }
  .hosts__caption{
    position:absolute;left:829px;top:370px;width:290px;text-align:center;
    font-size:19px;font-weight:600;letter-spacing:.5px;white-space:nowrap;
  }
  .portrait--guest{
    left:929px;top:683px;width:190px;height:190px;
    background:radial-gradient(circle at 50% 45%,#7a5038,#5c5c5c 60%,#d9e0dc);
  }
  .brand-panel{
    position:absolute;left:80px;top:459px;width:335px;height:410px;background:var(--ink);
    display:flex;align-items:center;justify-content:center;
  }
  .brand-panel__rule{
    position:absolute;left:12px;top:12px;right:12px;bottom:12px;border:2px solid var(--gold);
  }
  .brand-panel__name{font-size:34px;font-weight:600;color:var(--cream);letter-spacing:1px}
  .times{
    position:absolute;left:486px;top:459px;width:631px;height:189px;border-radius:34px;
    background:var(--cream);overflow:hidden;
  }
  .times__heading{
    height:84px;background:var(--ink);color:var(--cream);font-size:58px;font-weight:500;
    padding-left:24px;display:flex;align-items:center;letter-spacing:1px;
  }
  .times__list{list-style:none;color:var(--ink);font-size:34px;font-weight:500;padding:6px 0 0 24px;line-height:44px}
  .sunday__date{
    position:absolute;left:486px;top:682px;width:431px;height:36px;border-radius:10px;
    background:var(--cream);color:var(--ink);font-size:25px;font-weight:500;
    display:flex;align-items:center;padding-left:12px;
  }
  .sunday__service{position:absolute;left:486px;top:727px;font-size:26px;font-weight:700;white-space:nowrap}
  .sunday__evening-time{position:absolute;left:486px;top:776px;font-size:36px;font-weight:500}
  .sunday__evening-name{
    position:absolute;left:486px;top:824px;font-family:"Barlow Semi Condensed",sans-serif;
    font-size:34px;font-weight:500;white-space:nowrap;
  }
</style>
</head>
<body>
<main class="flyer">
  <div class="flyer__backdrop" role="img" aria-label="Red-tinted photograph of a worship hall stage with lights and audience"></div>
  <div class="flyer__frame"></div>

  <p class="event">SUMMIT GATHERING 2021 <span class="event__dates">· AUGUST 20TH–22ND</span></p>
  <h1 class="title"><span class="title__bold">GRACE</span><span class="title__boxed">TABERNACLE</span></h1>

  <p class="venue__label">VENUE:</p>
  <p class="venue__address">Sealand Gateway Lodgeview. 4817 North 239th Avenue Seattle, WA 98174.</p>

  <p class="guest__tag">GUEST MINISTER</p>
  <p class="guest__name">Bishop Lucinda Okotieno.<span class="guest__church">(Cedar Ridge Awakening)</span></p>

  <div class="portrait portrait--hosts" role="img" aria-label="Photo of hosts Pastors Ron n Della"></div>
  <p class="hosts__caption">Hosts: Pastors Ron n Della</p>

  <div class="brand-panel">
    <div class="brand-panel__rule"></div>
    <span class="brand-panel__name">Grace Tabernacle</span>
  </div>

  <section class="times">
    <h2 class="times__heading">CONFERENCE TIMES</h2>
    <ul class="times__list">
      <li>Friday August 20th 6pm-8:30pm</li>
      <li>Saturday August 21st 6pm-8:30pm</li>
    </ul>
  </section>

  <p class="sunday__date">Sunday August 22nd 10am-1pm</p>
  <p class="sunday__service">“CHURCH RENEWAL GATHERING”</p>
  <p class="sunday__evening-time">5pm-7:30pm</p>
  <p class="sunday__evening-name">TWOFOLD SURGE GATHERING.</p>

  <div class="portrait portrait--guest" role="img" aria-label="Photo of guest minister Bishop Lucinda Okotieno"></div>
</main>
</body>
</html>
```